Stationery Required - Own Logo provided

Hi,

We are a retail company called 'Bramwick Carto Limited' based in the UK and would like some corporate stationery designed.

We have provided our Logo which we would like to use (Its attached to this brief)...

The designs must be orginal, professional, stylish and interesting!

Target Market(s)

We will use this stationery to communicate with our wholesale suppliers and employees, so it must have a 'professional' feel about it.

Industry/Entity Type

It Company

Requirements
Must have
• Must be professional, corporate, stylish and not to 'fussy'. we require ... Business card design, a4 letter, compliment slip. All designs must be supplied in a format where the text (address/telephone numbers etc..) can be edited, as we have alot of staff and operate out of several different premises.
Nice to have
• I would like a windows backround picture file supplied as well so we can integrate that onto our computer systems.

```html
<!DOCTYPE html>
<html lang="en">
<head>
<meta charset="utf-8">
<title>Bramwick Carto Limited — Stationery</title>
<link href="https://fonts.googleapis.com/css2?family=Open+Sans:wght@400;600;700&display=swap" rel="stylesheet">
<style>
  :root{
    --forest:#3b5426;
    --lime:#8dc63f;
    --ink:#333a2c;
    --paper:#ffffff;
    --ground:#d9d6d2;
    --mist:#eeeeea;
    --pale:#f2f7ea;
  }
  *{box-sizing:border-box;margin:0;padding:0}
  html,body{width:1200px;height:900px;overflow:hidden}
  body{background:var(--ground);font-family:"Open Sans",Arial,sans-serif;color:var(--ink);position:relative}
  .sheet{position:absolute;background:var(--paper);overflow:hidden;box-shadow:0 2px 6px rgba(0,0,0,.18)}
  .brand{font-weight:600;color:var(--forest);letter-spacing:.01em;display:flex;align-items:center;gap:6px;white-space:nowrap}
  .brand .dot{display:inline-block;background:var(--lime);flex:none}
  .brand.on-dark{color:#fff}
  .band{position:absolute;left:0;right:0;bottom:0;background:var(--forest)}
  .contact{display:flex;font-size:11px;line-height:1.45;white-space:nowrap}
  .contact .col{padding-left:8px;border-left:1px solid var(--forest)}
  .contact .col + .col{margin-left:10px}
  .icon{display:inline-block;vertical-align:-1px;margin-right:3px}
  .web{color:#fff;letter-spacing:.18em;font-size:12px;white-space:nowrap}

  /* letterhead */
  .letterhead{left:38px;top:67px;width:548px;height:776px}
  .letterhead .brand{position:absolute;left:32px;top:24px;font-size:19px}
  .letterhead .brand .dot{width:14px;height:14px}
  .letterhead .wash{position:absolute;left:110px;top:365px;width:438px;height:330px;background:linear-gradient(160deg,var(--pale),var(--mist))}
  .letterhead .contact{position:absolute;left:32px;bottom:30px}
  .letterhead .band{height:21px}

  /* business cards */
  .card-front{left:657px;top:98px;width:231px;height:133px}
  .card-front .brand{position:absolute;right:10px;top:8px;font-size:12px}
  .card-front .brand .dot{width:9px;height:9px}
  .card-front .person{position:absolute;left:16px;top:60px}
  .card-front .name{font-size:10px;font-weight:700;color:var(--forest)}
  .card-front .role{font-size:6px}
  .card-front .details{position:absolute;left:16px;top:88px;font-size:6px;line-height:1.5}
  .card-front .band{height:8px}
  .card-back{left:907px;top:98px;width:234px;height:133px;background:var(--forest)}
  .card-back .block{position:absolute;left:0;top:0;width:92px;height:133px;background:var(--lime)}
  .card-back .brand{position:absolute;left:100px;top:50px;font-size:10px;letter-spacing:0}
  .card-back .web{position:absolute;left:100px;top:70px;font-size:6.5px;letter-spacing:.08em}

  /* compliment slip */
  .slip{left:621px;top:266px;width:549px;height:260px}
  .slip .brand{position:absolute;left:24px;top:22px;font-size:13px}
  .slip .brand .dot{width:11px;height:11px}
  .slip .greeting{position:absolute;left:24px;top:60px;font-size:17px;font-weight:700;color:var(--forest)}
  .slip .contact{position:absolute;left:232px;top:18px;font-size:9.5px}
  .slip .band{height:21px}
  .slip .web{position:absolute;right:20px;bottom:3px}

  /* envelope panel */
  .panel{left:621px;top:553px;width:549px;height:258px;background:var(--forest)}
  .panel .block{position:absolute;left:0;top:0;width:230px;height:258px;background:var(--lime)}
  .panel .inset{position:absolute;left:0;top:92px;width:130px;height:166px;background:var(--paper)}
  .panel .brand{position:absolute;left:268px;top:104px;font-size:20px}
  .panel .web{position:absolute;left:268px;top:140px;font-size:12px;letter-spacing:.14em}
</style>
</head>
<body>

<section class="sheet letterhead" aria-label="A4 letterhead">
  <div class="brand"><span class="dot"></span>Bramwick Carto Limited</div>
  <div class="wash"></div>
  <div class="contact">
    <div class="col">17 mill brae road, Larchfield<br>County Antrim BT41 3QP</div>
    <div class="col">
      <svg class="icon" width="10" height="9" viewBox="0 0 10 9"><path d="M1 3c2-3 6-3 8 0l-2 1-1-1H4L3 4z M2 5h6v3H2z" fill="#8dc63f"/></svg>:0770-900-4123<br>
      <svg class="icon" width="10" height="8" viewBox="0 0 10 8"><rect x=".5" y=".5" width="9" height="7" fill="none" stroke="#8dc63f"/><path d="M.5 .5l4.5 4 4.5-4" fill="none" stroke="#8dc63f"/></svg>:hello@bramwickcarto.co.uk
    </div>
  </div>
  <div class="band"></div>
</section>

<section class="sheet card-front" aria-label="Business card front">
  <div class="brand"><span class="dot"></span>Bramwick Carto Limited</div>
  <div class="person"><div class="name">Owen Harlow</div><div class="role">Company Director</div></div>
  <div class="details">17 mill brae road, Larchfield<br>County Antrim BT41 3QP<br>☎ :0770-900-4123<br>✉ :hello@bramwickcarto.co.uk</div>
  <div class="band"></div>
</section>

<section class="sheet card-back" aria-label="Business card back">
  <div class="block"></div>
  <div class="brand on-dark">Bramwick Carto Limited</div>
  <div class="web">www.bramwickcarto.co.uk</div>
</section>

<section class="sheet slip" aria-label="Compliment slip">
  <div class="brand"><span class="dot"></span>Bramwick Carto Limited</div>
  <div class="greeting">With Compliments</div>
  <div class="contact">
    <div class="col">17 mill brae road, Larchfield<br>County Antrim BT41 3QP</div>
    <div class="col">☎ :0770-900-4123<br>✉ :hello@bramwickcarto.co.uk</div>
  </div>
  <div class="band"></div>
  <div class="web">www.bramwickcarto.co.uk</div>
</section>

<section class="sheet panel" aria-label="Envelope">
  <div class="block"></div>
  <div class="inset"></div>
  <div class="brand on-dark">Bramwick Carto Limited</div>
  <div class="web">www.bramwickcarto.co.uk</div>
</section>

</body>
</html>
```